Modern Business Card Design Needed for Young Realtor

Information that is going on the card:Marvin Pold
Broker/Owner
555.210.3367
Marvin@MPoldRealty.com
www.MPoldRealty.com

Would also like to include my Instagram Handle somewhere. Probably on the back: the_queencity_realtorMy previous business card is attached, I like that one but would like an updated version and maybe a few design changes

Marvin Pold
Broker/Owner
555.210.3367
Marvin@MPoldRealty.com
www.MPoldRealty.com

• Would also like to include my Instagram Handle somewhere. Probably on the back: the_pinecrest_realtor
• Dorrance Hale or the DH (logo from the previous card.)

```html
<!DOCTYPE html>
<html lang="en">
<head>
<meta charset="utf-8">
<title>MPold Realty Business Card</title>
<link rel="stylesheet" href="https://fonts.googleapis.com/css2?family=Libre+Baskerville:wght@400&family=PT+Sans:wght@400&display=swap">
<style>
  :root {
    --bg: #6f6d69;
    --card: #ffffff;
    --ink: #1e1e1e;
    --accent: #b01c26;
    --rule: #8a8a8a;
    --photo-a: #7f9a68;
    --photo-b: #4a4640;
  }
  * { margin: 0; padding: 0; box-sizing: border-box; }
  html, body { width: 1200px; height: 856px; overflow: hidden; }
  body {
    background: var(--bg);
    font-family: "Libre Baskerville", Georgia, serif;
    color: var(--ink);
    position: relative;
  }
  .card {
    position: absolute;
    top: 278px;
    width: 520px;
    height: 300px;
    background: var(--card);
    border-radius: 26px;
    box-shadow: 0 6px 18px rgba(0,0,0,0.25);
  }
  .card--front { left: 50px; }
  .card--back { left: 630px; }

  .brand {
    position: absolute;
    white-space: nowrap;
  }
  .brand__name {
    letter-spacing: 0.2em;
    color: var(--accent);
    line-height: 1;
  }
  .brand__rule {
    height: 1px;
    background: var(--rule);
    margin-top: 6px;
  }
  .card--front .brand { left: 40px; top: 76px; }
  .card--front .brand__name { font-size: 20px; }
  .card--back .brand { left: 50%; top: 110px; transform: translateX(-50%); }
  .card--back .brand__name { font-size: 25px; letter-spacing: 0.26em; }

  .contact {
    position: absolute;
    left: 40px;
    top: 132px;
    width: 232px;
    text-align: center;
  }
  .contact__name {
    font-size: 21px;
    letter-spacing: 0.02em;
    line-height: 1.1;
  }
  .contact__first { color: var(--accent); }
  .contact__role {
    font-size: 14px;
    margin-top: 2px;
  }
  .contact__lines {
    margin-top: 16px;
    font-size: 14px;
    line-height: 1.45;
  }
  .contact__web-domain { color: var(--accent); }

  .portrait {
    position: absolute;
    right: 28px;
    top: 55px;
    width: 190px;
    height: 190px;
    border-radius: 50%;
    border: 2px solid var(--ink);
    box-shadow: inset 0 0 0 1px var(--accent);
    background: radial-gradient(circle at 50% 40%, var(--photo-b) 0%, var(--photo-b) 38%, var(--photo-a) 72%);
  }

  .handle {
    position: absolute;
    left: 0;
    right: 0;
    top: 178px;
    text-align: center;
    font-family: "PT Sans", Arial, sans-serif;
    font-size: 14px;
    letter-spacing: 0.04em;
  }
</style>
</head>
<body>
  <section class="card card--front" aria-label="Business card front">
    <div class="brand">
      <div class="brand__name">MPOLD REALTY</div>
      <div class="brand__rule"></div>
    </div>

    <div class="contact">
      <p class="contact__name"><span class="contact__first">MARVIN</span> POLD</p>
      <p class="contact__role">Broker/Owner</p>
      <div class="contact__lines">
        <p>555.210.3367</p>
        <p>Marvin@MPoldRealty.com</p>
        <p>www.<span class="contact__web-domain">MPoldRealty</span>.com</p>
      </div>
    </div>

    <div class="portrait" role="img" aria-label="Circular portrait photo of the broker outdoors"></div>
  </section>

  <section class="card card--back" aria-label="Business card back">
    <div class="brand">
      <div class="brand__name">MPOLD REALTY</div>
      <div class="brand__rule"></div>
    </div>
    <p class="handle">the_pinecrest_realtor</p>
  </section>
</body>
</html>
```